Wedding Invitation and Logo

We would like an invitation and logo designed for our wedding on October 19, 2019 in Charlotte, NC. Our names are Mara and Cobb, we met in school at Brindlemoor Valley College, and we got engaged at a fire tower which has a view down to the campus. You do not have to include these, but some ideas for the invitation design would be mountains, a fire tower, our initials, or the city. The wedding will be at 4:30 in the afternoon with a reception to follow. We do not need to list the families as there are four of them and that is too much info. The colors we would like to use are white, black, royal blue, and maybe silver. Do not feel obligated to use them all though.We would like the logo to include similar elements such as mountains, fire tower, or our initials(M and C). The logo can be a one color design as we may use it on our cake, as light filters to be displayed on the walls at our reception, or as an accent on name plates and stationery.We like simple, clean designs and our wedding will have a wintery theme (white linens, white chair covers, silver and royal blue accents, etc.).Things we do not want: snowflakes, flowers, polka dots, leaves, gold foil.Thank you!

Font styles to use
Serif
Script

Requirements
Must have
• Some combination of white, black, royal blue, optionally silver.
Nice to have
• Mountains, fire tower, our initials (M and C), wintry theme (no snowflakes)
Should not have
• Snowflakes, flowers, polka dots, leaves, gold foil

```html
<!DOCTYPE html>
<html lang="en">
<head>
<meta charset="utf-8">
<title>Save the Date – Mara &amp; Cobb</title>
<link rel="stylesheet" href="https://fonts.googleapis.com/css2?family=Cinzel:wght@700;900&family=Open+Sans:wght@400&family=Yellowtail&family=Oswald:wght@300;700&display=swap">
<style>
  :root {
    --backdrop: #1f1f20;
    --royal-blue: #1537c9;
    --ink: #2b2d2e;
    --white: #ffffff;
    --snow: #f6fbfb;
    --ice: #d9f0f1;
    --silver: #b9bebe;
  }
  * { margin: 0; padding: 0; box-sizing: border-box; }
  html, body {
    width: 1200px; height: 900px; overflow: hidden;
    background: var(--backdrop);
  }
  .canvas { position: relative; width: 1200px; height: 900px; }

  .card {
    position: absolute; left: 367px; top: 152px;
    width: 481px; height: 683px;
    background: var(--snow);
    border: 14px solid var(--royal-blue);
    overflow: hidden;
    text-align: center;
    color: var(--ink);
  }
  .card__scene {
    position: absolute; inset: 0;
    background:
      linear-gradient(180deg, var(--snow) 0%, #eef5f5 22%, #c9cfcf 48%, #dfeff0 70%, var(--ice) 100%);
  }

  .monogram {
    position: absolute; left: 0; right: 0; top: 36px;
    display: flex; align-items: center; justify-content: center; gap: 8px;
    font-family: "Cinzel", serif; font-weight: 700; font-size: 22px;
    color: var(--royal-blue);
  }
  .monogram__circle {
    width: 22px; height: 22px; border-radius: 50%;
    border: 3px solid var(--royal-blue);
  }

  .headline { position: absolute; left: 20px; top: 92px; width: 425px; height: 80px; }
  .headline text {
    font-family: "Cinzel", serif; font-weight: 900; font-size: 44px;
    fill: var(--ink); stroke: var(--white); stroke-width: 1.5px; paint-order: stroke;
    letter-spacing: -1px;
  }

  .invite {
    position: absolute; left: 0; right: 0; top: 198px;
    font-family: "Open Sans", sans-serif; font-size: 22px; line-height: 25px;
    color: var(--ink);
  }

  .couple {
    position: absolute; left: 0; right: 0; top: 268px;
    font-family: "Yellowtail", cursive; color: var(--royal-blue);
    line-height: 1;
  }
  .couple__name { display: block; font-size: 64px; }
  .couple__amp { display: block; font-size: 44px; color: var(--white); margin: -2px 0 -6px; }

  .date {
    position: absolute; left: 0; right: 0; top: 544px;
    font-family: "Oswald", sans-serif; color: var(--ink);
    line-height: 1;
  }
  .date__day { font-size: 40px; }
  .date__day strong { font-weight: 700; }
  .date__day span { font-weight: 300; }
  .date__time { display: block; margin-top: 6px; font-size: 27px; font-weight: 300; }
  .date__time strong { font-weight: 700; color: var(--royal-blue); }
  .date__time em { font-style: normal; color: var(--royal-blue); }
</style>
</head>
<body>
<main class="canvas">
  <article class="card">
    <div class="card__scene" role="img" aria-label="Winter scene: snowy mountain peaks, silver pine forest and a fire lookout tower standing on snowy ground"></div>

    <div class="monogram"><span class="monogram__circle"></span>M and C</div>

    <svg class="headline" viewBox="0 0 425 80" aria-label="Save the Date">
      <defs>
        <path id="headline-arc" d="M 8 72 Q 212 20 417 72"/>
      </defs>
      <text><textPath href="#headline-arc" startOffset="50%" text-anchor="middle">SAVE THE DATE</textPath></text>
    </svg>

    <p class="invite">Invite you to celebrate<br>our wedding</p>

    <h1 class="couple">
      <span class="couple__name">Mara</span>
      <span class="couple__amp">&amp;</span>
      <span class="couple__name">Cobb</span>
    </h1>

    <p class="date">
      <span class="date__day"><strong>19th</strong> <span>October</span> <strong>2019</strong></span>
      <span class="date__time">at <strong>4.30</strong> <em>p.m</em></span>
    </p>
  </article>
</main>
</body>
</html>
```